Vantel Solutions Website Design

We are a B2B startup offering a free virtual data room and deal management platform for small businesses. We need a 10-page website geared towards business executives and entrepreneurs that is simple, uploads quickly and provides a good introduction to our product. We've attached a document setting forth the text of 8 of the 10 pages (the other two - Resources and Blog - need to be designed to allow the future posting of white papers and blog entries) and links to the screenshots and GIFs, all of which are in a folder on filewell. We've also attached a zip file with our logo and a pdf file with our font and colors. Examples of websites we like include www.marbletoft.example, www.usepivra.example and https://kelmo.example.

Target Market(s)

Small business owners, business executives and entrepreneurs

Industry/Entity Type

Finance

Coding

Number of Pages Required

5+ page

Font styles to use
Sans Serif

Colors
85abd2
f9ba93

Requirements
Must have
• Please use the Wordpress harbor theme I uploaded to code the site.
Nice to have
• Clean, uncluttered design. White background. Screenshots and gifs should be shown on monitors (desktop, laptop and iPad only). Blue and orange are our corporate colors, but you’re not limited to those two colors. See uploaded logo guide for complementary colors or use your own judgment.

```html
<!DOCTYPE html>
<html lang="en">
<head>
<meta charset="utf-8">
<title>Vantel — Getting your workflow flowing</title>
<link href="https://fonts.googleapis.com/css2?family=Outfit:wght@400;500;700&display=swap" rel="stylesheet">
<style>
  :root {
    --orange: #e8662a;
    --slate: #3d5f75;
    --ink: #2b2b2b;
    --muted: #7a7a7a;
    --faint: #c9c9c9;
    --rule: #d6d6d6;
    --blob: #eceef1;
    --sun: #fbd89c;
    --sky: #e3eef5;
    --white: #ffffff;
  }
  * { margin: 0; padding: 0; box-sizing: border-box; }
  html, body { width: 1200px; height: 823px; overflow: hidden; background: var(--white); }
  body { position: relative; font-family: "Outfit", sans-serif; color: var(--ink); }

  .brand { position: absolute; left: 114px; top: 33px; font-size: 31px; font-weight: 500; color: var(--slate); letter-spacing: -0.5px; }

  .main-nav { position: absolute; top: 43px; left: 0; font-size: 15px; }
  .main-nav a { position: absolute; white-space: nowrap; color: var(--ink); text-decoration: none; display: flex; align-items: center; gap: 6px; }
  .main-nav svg { width: 8px; height: 5px; }
  .cta { position: absolute; left: 950px; top: 30px; width: 136px; height: 48px; border-radius: 24px; background: var(--orange); color: var(--white); font-size: 12px; font-weight: 700; display: flex; align-items: center; justify-content: center; letter-spacing: 0.2px; }

  .hero-title { position: absolute; left: 113px; top: 154px; font-size: 52px; font-weight: 400; line-height: 57px; color: var(--orange); letter-spacing: -0.5px; }
  .hero-lead { position: absolute; left: 114px; top: 294px; width: 340px; font-size: 17px; line-height: 21px; color: var(--ink); }

  .benefits { position: absolute; left: 114px; top: 384px; width: 285px; list-style: none; }
  .benefit { display: flex; align-items: center; gap: 18px; height: 58px; border-bottom: 1px solid var(--rule); font-size: 14px; line-height: 16.5px; }
  .benefit:first-child { height: 53px; }
  .benefit:last-child { border-bottom: none; }
  .benefit svg { width: 32px; height: 32px; flex: none; }

  .hero-art { position: absolute; left: 592px; top: 164px; width: 554px; height: 416px; background: var(--blob); border-radius: 46% 54% 40% 60% / 42% 38% 62% 58%; }

  .dot-sun { position: absolute; left: 911px; top: 620px; width: 31px; height: 33px; border-radius: 48% 52% 55% 45%; background: var(--sun); }
  .crescent { position: absolute; left: 207px; top: 658px; width: 52px; height: 30px; }

  .testimonial { position: absolute; left: 238px; top: 636px; width: 724px; height: 130px; background: var(--white); border-radius: 8px; box-shadow: 0 4px 28px rgba(0,0,0,0.06); text-align: center; padding-top: 24px; }
  .testimonial blockquote { font-size: 20px; line-height: 26px; color: var(--muted); width: 540px; margin: 0 auto; }
  .testimonial cite { display: block; margin-top: 16px; font-style: normal; font-size: 11.5px; color: var(--faint); }
</style>
</head>
<body>
  <header>
    <div class="brand">Vantel</div>
    <nav class="main-nav">
      <a style="left:413px">Features <svg viewBox="0 0 8 5"><path d="M0 0h8L4 5z" fill="#666"/></svg></a>
      <a style="left:507px">Customers</a>
      <a style="left:606px">Company <svg viewBox="0 0 8 5"><path d="M0 0h8L4 5z" fill="#666"/></svg></a>
      <a style="left:707px">Get in touch</a>
    </nav>
    <div class="cta">TRY IT NOW</div>
  </header>

  <section class="hero">
    <h1 class="hero-title">Getting your<br>workflow flowing</h1>
    <p class="hero-lead">The Vantel assistant is a secure, sharable workflow management platform designed with your needs in mind.</p>
    <ul class="benefits">
      <li class="benefit">
        <svg viewBox="0 0 32 32"><circle cx="10" cy="10" r="5" fill="#e8662a"/><circle cx="23" cy="12" r="4" fill="#e8662a"/><path d="M0 26c0-6 4-9 10-9s10 3 10 9z" fill="#e8662a"/><path d="M17 26c1-5 3-8 7-8s8 3 8 8z" fill="#e8662a"/></svg>
        <span>Built for internal<br>and external collaboration</span>
      </li>
      <li class="benefit">
        <svg viewBox="0 0 32 32" fill="none" stroke="#e8662a" stroke-width="2.6" stroke-linecap="round"><path d="M21 9c-2-2-9-2-9 2s9 3 9 7-7 4-10 2"/><path d="M16 3v4M16 23v5"/><path d="M5 4l22 24"/></svg>
        <span>Free to use – no setup<br>or monthly fees</span>
      </li>
      <li class="benefit">
        <svg viewBox="0 0 32 32"><path d="M2 2h28v22H9l-7 6z" fill="#e8662a"/><path d="M8 18l9-9 3 3-9 9H8zM9 21h15" stroke="#fff" stroke-width="2" fill="none"/></svg>
        <span>Highly intuitive<br>and customizable</span>
      </li>
    </ul>
    <div class="hero-art" role="img" aria-label="Illustration of three people pinning message cards onto a soft grey shape"></div>
  </section>

  <svg class="crescent" viewBox="0 0 52 30"><path d="M0 4c10 4 30 6 52-2-2 16-14 26-28 26C10 28 2 18 0 4z" fill="#e3eef5"/></svg>
  <section class="testimonial">
    <blockquote>“Efficient workflow management has resulted in an 85% savings in deal closings over the past six years.”</blockquote>
    <cite>The Global Council for Contract and Deal Operations</cite>
  </section>
  <div class="dot-sun"></div>
</body>
</html>
```